Online plant nursery needs3 seperate slides for a intro web site slide slide show

We need 3 slide graphics / banners measurments should be 960wide 540 tall and 2mb or smaller. We are an online mail order nursery that focuses sales on Peonies.
Slide 1: Use faded out photos of Peony Garden with many flowers just budding. Our logo and the Words "A Lost Spring is Never Found Again". try to use our logo in a small small watermark on all slides.
Slide 2: Use your own creativity for the slide.... message should say "Free Shipping"
Slide 3: Use your own creativity for the slide .... messgae "Shop Our Other Items". To see site it will be used on go to http://k4830157.tbrwxq9pnlhe.preview82.shopnestle-example.com/

Target Market(s)

home owners age 30 - 65.

Industry/Entity Type

Nursery

Requirements
Must have
• must transition well.
Should not have
• can not be larger than 2MB per file

```html
<!DOCTYPE html>
<html lang="en">
<head>
<meta charset="utf-8">
<title>Shop Our Other Items</title>
<link rel="stylesheet" href="https://fonts.googleapis.com/css2?family=Yellowtail&display=block">
<style>
  :root {
    --deep-red: #a8200f;
    --brick: #c4391c;
    --orange: #dc6233;
    --peach: #eaa07e;
    --blush: #f4c9b4;
    --white: #ffffff;
  }
  html, body {
    margin: 0;
    padding: 0;
    width: 1200px;
    height: 675px;
    overflow: hidden;
    background: var(--deep-red);
  }
  .slide {
    position: relative;
    width: 1200px;
    height: 675px;
    overflow: hidden;
  }
  .slide__pattern {
    position: absolute;
    inset: 0;
    background:
      radial-gradient(ellipse 38% 45% at 50% 28%, rgba(244, 201, 180, 0.85), rgba(244, 201, 180, 0) 70%),
      radial-gradient(ellipse 30% 40% at 52% 88%, rgba(234, 160, 126, 0.7), rgba(234, 160, 126, 0) 70%),
      radial-gradient(ellipse 35% 55% at 8% 45%, rgba(168, 32, 15, 0.9), rgba(168, 32, 15, 0) 75%),
      radial-gradient(ellipse 35% 55% at 95% 40%, rgba(168, 32, 15, 0.85), rgba(168, 32, 15, 0) 75%),
      linear-gradient(135deg, var(--brick) 0%, var(--orange) 35%, var(--peach) 50%, var(--orange) 68%, var(--brick) 100%);
  }
  .slide__frame {
    position: absolute;
    left: 60px;
    top: 91px;
    width: 1080px;
    height: 480px;
    border: 2px solid var(--white);
    box-sizing: border-box;
  }
  .slide__headline {
    position: absolute;
    left: 80px;
    right: 80px;
    top: 270px;
    margin: 0;
    text-align: center;
    font-family: "Yellowtail", "Brush Script MT", cursive;
    font-weight: 400;
    font-size: 118px;
    line-height: 1;
    color: var(--white);
    white-space: nowrap;
  }
</style>
</head>
<body>
  <main class="slide">
    <div class="slide__pattern" role="img" aria-label="Abstract pattern of overlapping translucent circles in deep red, orange and peach tones"></div>
    <div class="slide__frame"></div>
    <h1 class="slide__headline">Shop Our Other Items</h1>
  </main>
</body>
</html>
```